Mr. Kelpfin Restaurant Menu Design

I would like for you to please create a menu design for my seafood restaurant called Mr. Kelpfin. I uploaded the logo of my restaurant and would like the same colors and font to be used on the menu. The headings of my menu should include the following:
What's your catch?
What's your sauce?
How "Hot" can you go?
Medium?
Mild?
Wild?
Soups
Paella
Katsu
Add Ons
Sweet Cravings
Thirsty?
It would be nice to see something creative and simple preferably one page.
I already uploaded my logo on the brief section.
Thank you.
Target Market(s)
Family friendly
Industry/Entity Type
Seafood Restaurant
Look and feel

```html
<!DOCTYPE html>
<html lang="en">
<head>
<meta charset="utf-8">
<title>Mr. Kelpfin Restaurant Menu</title>
<link href="https://fonts.googleapis.com/css2?family=Fredoka:wght@600&family=Oswald:wght@400&display=swap" rel="stylesheet">
<style>
  :root{
    --page:#ffffff;
    --sea-deep:#1f8fd8;
    --sea-mid:#4fb3ec;
    --sea-light:#a9ddf7;
    --card-top:#ffffff;
    --card-bottom:#8fd3f2;
    --wood-dark:#7a4a26;
    --wood-light:#c08a58;
    --heading:#ffffff;
    --heading-edge:#1aa6dc;
    --item:#6b3412;
    --brand:#1b1b1b;
    --brand-sub:#1a8fd6;
    --brand-accent:#f08a1c;
    --food-a:#c9b69a;
    --food-b:#e0843e;
    --food-c:#7e8f95;
  }
  *{box-sizing:border-box;margin:0;padding:0}
  html,body{width:1200px;height:1000px;overflow:hidden;background:var(--page)}
  .menu{
    position:absolute;left:287px;top:60px;width:620px;height:867px;overflow:hidden;
    background:
      radial-gradient(ellipse at 50% 8%,rgba(255,255,255,.55),transparent 45%),
      linear-gradient(180deg,var(--sea-light) 0%,var(--sea-mid) 35%,var(--sea-deep) 75%,var(--sea-mid) 100%);
    font-family:"Oswald",sans-serif;
  }
  .brand{position:absolute;left:200px;top:30px;width:220px;text-align:center}
  .brand-mark{width:48px;height:48px;border-radius:50%;background:var(--brand-accent);margin:0 auto 56px}
  .brand-name{font-family:"Fredoka",sans-serif;font-weight:600;font-size:32px;line-height:36px;color:var(--brand);white-space:nowrap}
  .brand-sub{font-family:"Fredoka",sans-serif;font-weight:600;font-size:15px;line-height:18px;color:var(--brand-sub)}
  .menu-title{position:absolute;left:200px;top:186px;width:220px;text-align:center;
    font-family:"Fredoka",sans-serif;font-weight:600;font-size:34px;line-height:42px;color:var(--brand)}
  .plate{position:absolute;height:24px;
    background:linear-gradient(180deg,var(--wood-light),var(--wood-dark));
    border-radius:2px;box-shadow:0 2px 3px rgba(0,0,0,.35);
    font-family:"Fredoka",sans-serif;font-weight:600;font-size:16px;line-height:24px;text-align:center;white-space:nowrap;
    color:var(--heading);text-shadow:-1px -1px 0 var(--heading-edge),1px -1px 0 var(--heading-edge),-1px 1px 0 var(--heading-edge),1px 1px 0 var(--heading-edge);z-index:2}
  .card{position:absolute;width:154px;border-radius:6px;
    background:linear-gradient(180deg,var(--card-top) 35%,var(--card-bottom));
    box-shadow:0 3px 6px rgba(0,40,90,.35);padding-left:36px}
  .card li{list-style:none;font-size:11px;color:var(--item);height:26px;line-height:26px;white-space:nowrap}
  .food{position:absolute;left:0;top:740px;width:620px;height:127px;z-index:3;
    background:linear-gradient(90deg,var(--food-a),var(--food-c) 25%,var(--food-b) 55%,#d9c4a4 80%,var(--food-b));
    clip-path:polygon(0 0,6% 5%,8% 30%,30% 35%,38% 50%,50% 60%,65% 58%,72% 50%,80% 40%,100% 30%,100% 100%,0 100%)}
</style>
</head>
<body>
<main class="menu">
  <div class="brand">
    <div class="brand-mark"></div>
    <div class="brand-name">Mr. Kelpfin</div>
    <div class="brand-sub">Restaurant</div>
  </div>
  <h1 class="menu-title">Menu</h1>

  <div class="plate" style="left:13px;top:65px;width:203px">What's your catch?</div>
  <ul class="card" style="left:33px;top:80px;height:140px;padding-top:7px;padding-left:38px"><li>Dish.....................00</li><li>Dish.....................00</li><li>Dish.....................00</li><li>Dish.....................00</li><li>Dish.....................00</li></ul>

  <div class="plate" style="left:400px;top:65px;width:203px">What's your Sauce?</div>
  <ul class="card" style="left:423px;top:80px;height:142px;padding-top:7px;padding-left:37px"><li>Sauce....................00</li><li>Sauce....................00</li><li>Sauce....................00</li><li>Sauce....................00</li><li>Sauce....................00</li></ul>

  <div class="plate" style="left:203px;top:230px;width:217px;height:25px;line-height:25px">How "Hot" can you go?</div>

  <div class="plate" style="left:43px;top:261px;width:133px">Medium?</div>
  <ul class="card" style="left:37px;top:264px;height:146px;padding-top:18px;padding-left:34px"><li>Medium................00</li><li>Medium................00</li><li>Medium................00</li><li>Medium................00</li><li>Medium................00</li></ul>
  <div class="plate" style="left:241px;top:261px;width:133px">Mild?</div>
  <ul class="card" style="left:234px;top:264px;height:146px;padding-top:18px;padding-left:36px"><li>Mild.....................00</li><li>Mild.....................00</li><li>Mild.....................00</li><li>Mild.....................00</li><li>Mild.....................00</li></ul>
  <div class="plate" style="left:433px;top:261px;width:133px">Wild?</div>
  <ul class="card" style="left:425px;top:264px;height:146px;padding-top:18px;padding-left:40px"><li>Wild.....................00</li><li>Wild.....................00</li><li>Wild.....................00</li><li>Wild.....................00</li><li>Wild.....................00</li></ul>

  <div class="plate" style="left:47px;top:437px;width:133px">Soups</div>
  <ul class="card" style="left:37px;top:445px;height:158px;padding-top:21px;padding-left:34px"><li>Soups...................00</li><li>Soups...................00</li><li>Soups...................00</li><li>Soups...................00</li><li>Soups...................00</li></ul>
  <div class="plate" style="left:240px;top:437px;width:133px">Paella</div>
  <ul class="card" style="left:232px;top:445px;height:158px;padding-top:21px;padding-left:37px"><li>Paella..................00</li><li>Paella..................00</li><li>Paella..................00</li><li>Paella..................00</li><li>Paella..................00</li></ul>
  <div class="plate" style="left:435px;top:437px;width:133px">Katsu</div>
  <ul class="card" style="left:427px;top:445px;height:158px;padding-top:21px;padding-left:38px"><li>Katsu...................00</li><li>Katsu...................00</li><li>Katsu...................00</li><li>Katsu...................00</li><li>Katsu...................00</li></ul>

  <div class="plate" style="left:48px;top:632px;width:133px">Add Ons</div>
  <ul class="card" style="left:40px;top:642px;height:210px;padding-top:24px;padding-left:31px"><li>Add Ons..................00</li><li>Add Ons..................00</li><li>Add Ons..................00</li><li>Add Ons..................00</li></ul>
  <div class="plate" style="left:241px;top:632px;width:133px;font-size:14px">Sweet Cravings</div>
  <ul class="card" style="left:235px;top:642px;height:210px;padding-top:27px;padding-left:34px"><li>Sweet Carvings.......00</li><li>Sweet Carvings.......00</li><li>Sweet Carvings.......00</li><li>Sweet Carvings.......00</li></ul>
  <div class="plate" style="left:438px;top:632px;width:133px">Thirsty?</div>
  <ul class="card" style="left:430px;top:642px;height:210px;padding-top:23px;padding-left:34px"><li>Thirsty...................00</li><li>Thirsty...................00</li><li>Thirsty...................00</li><li>Thirsty...................00</li></ul>

  <div class="food" role="img" aria-label="Photo strip of seafood dishes: shrimp, dipping sauces, grilled fish with salad, and a crab platter"></div>
</main>
</body>
</html>
```